Floristry Business Card Design Project

I have a logo now and am looking to incorporate this into a business card. I would like a double sided business card. I would like one side to be decorative so that it blends well when included with floral arrangements and that can also be used as the front of a card and the other side will contain the business details. The font on the business details side should be clear although some decorative font would be ok. I have included the logo files for use in the business card design.

Feel free to break up the logo and use certain aspects of it in the design. Really looking for something that stands out and that is really creative.

Industry/Entity Type

Floral

Requirements
Should not have
• Nothing tacky or corny. The logo should be clearly read (perhaps a background colour).

```html
<!DOCTYPE html>
<html lang="en">
<head>
<meta charset="utf-8">
<title>Meadow Lane – Business Card</title>
<link href="https://fonts.googleapis.com/css2?family=Cinzel:wght@400;600&display=swap" rel="stylesheet">
<style>
  :root {
    --page-bg: #ffffff;
    --frame-line: #3a3a3a;
    --front-green: #c0cd84;
    --back-green: #90c2a2;
    --ink-white: #ffffff;
  }
  html, body {
    margin: 0;
    padding: 0;
    width: 1200px;
    height: 1000px;
    overflow: hidden;
    background: var(--page-bg);
  }
  .canvas {
    position: relative;
    width: 1200px;
    height: 1000px;
    box-sizing: border-box;
    border: 2px solid var(--frame-line);
  }
  .card {
    position: absolute;
    top: 266px;
    width: 427px;
    height: 467px;
    overflow: hidden;
  }
  .card--front { left: 170px; background: var(--front-green); }
  .card--back  { left: 603px; background: var(--back-green); }
  .card svg { position: absolute; inset: 0; }
  .ring { fill: none; stroke: var(--ink-white); }
  .wreath { fill-rule: evenodd; }
  .brand-name {
    position: absolute;
    left: 0;
    right: 0;
    top: 352px;
    margin: 0;
    text-align: center;
    font-family: "Cinzel", "Trajan Pro", serif;
    font-weight: 400;
    font-size: 29px;
    letter-spacing: 0.34em;
    padding-left: 0.34em;
    color: var(--ink-white);
  }
  .contact {
    position: absolute;
    left: 0;
    right: 0;
    top: 180px;
    margin: 0;
    text-align: center;
    font-family: "Cinzel", "Trajan Pro", serif;
    font-weight: 400;
    color: var(--ink-white);
    font-size: 22px;
    line-height: 26px;
  }
  .contact__label { display: block; }
  .contact__label--name { margin-bottom: 30px; font-weight: 600; }
</style>
</head>
<body>
<main class="canvas">

  <section class="card card--front" aria-label="Card front">
    <svg width="427" height="467" viewBox="0 0 427 467">
      <defs>
        <radialGradient id="front-wreath-tone" gradientUnits="userSpaceOnUse" cx="215" cy="215" r="132">
          <stop offset="0.64" stop-color="#ffffff" stop-opacity="0.55"/>
          <stop offset="0.8" stop-color="#ffffff" stop-opacity="0.4"/>
          <stop offset="1" stop-color="#ffffff" stop-opacity="0.08"/>
        </radialGradient>
      </defs>
      <path class="wreath" fill="url(#front-wreath-tone)" role="img"
            aria-label="Ring of white hand-drawn flowers, buds and leaves around the emblem"
            d="M215,83 a132,132 0 1,0 0.1,0 Z M215,129 a86,86 0 1,0 0.1,0 Z"/>
      <circle class="ring" cx="215" cy="215" r="84" stroke-width="1.6"/>
      <circle class="ring" cx="215" cy="215" r="79" stroke-width="1"/>
    </svg>
    <h1 class="brand-name">Meadow Lane</h1>
  </section>

  <section class="card card--back" aria-label="Card back">
    <svg width="427" height="467" viewBox="0 0 427 467">
      <defs>
        <radialGradient id="back-wreath-tone" gradientUnits="userSpaceOnUse" cx="214" cy="234" r="200">
          <stop offset="0.68" stop-color="#ffffff" stop-opacity="0.55"/>
          <stop offset="0.82" stop-color="#ffffff" stop-opacity="0.38"/>
          <stop offset="1" stop-color="#ffffff" stop-opacity="0.06"/>
        </radialGradient>
      </defs>
      <path class="wreath" fill="url(#back-wreath-tone)" role="img"
            aria-label="Ring of white hand-drawn flowers, buds and leaves framing the contact details"
            d="M214,34 a200,200 0 1,0 0.1,0 Z M214,97 a137,137 0 1,0 0.1,0 Z"/>
      <circle class="ring" cx="214" cy="234" r="135" stroke-width="2.4"/>
      <circle class="ring" cx="214" cy="234" r="126" stroke-width="1.4"/>
    </svg>
    <p class="contact">
      <span class="contact__label contact__label--name">Name:</span>
      <span class="contact__label">Email Address:</span>
      <span class="contact__label">Phone:</span>
    </p>
  </section>

</main>
</body>
</html>
```